Album Cover for upcoming release

Hi, I need an album cover for a song that I’ll be releasing soon. The album cover must contain the title of the song, which is:

Carry the Tide (remix)

The album cover must also contain the artist name:

Derek Hanmore

The song is a remix of a song that I released in late-May called “Carry the Tide.” I wrote the original song for my wife. If you’re interested, please give it a listen on Tunevault or Soundmarrow under the artist Derek Hanmore. Here’s a Soundmarrow link to the original song (it already has more than 175,000 streams):

https://play.soundmarrow.example/track/7RtZpLc92XGb4nHqWmEsVd?si=kd3TfPzX8wQmLr2NbYcVhe

The remix is VERY, VERY different! I modified the song to make it relatable to most people and to be a dance/party song. Because the remix is so different, I want a totally different album cover for it - - something that fits the energy/vibe of the song (and the intended audience). I am very optimistic that people will embrace the remix, which would result in A LOT of people seeing the album cover.

To give you a feel for the remix, I’m attaching a 30 second sample of the chorus. Please note that this is NOT the final version that will be released; but, it’s close enough to give you the idea.

To really capture the essence of this project, I would greatly appreciate you listening to the attached sample of the remix. Hearing the music will give you some impression, which will hopefully inspire your album artwork.

Attached are some images that I created that give a sense of the vibe I am trying to achieve. Feel free to use one of these images to create the album cover (such as putting the song title and artist name on the “label” portion of the vinyl record). But, you are NOT required to use one os these images.
Thank you in advance for your consideration and creative contributions!

Target Market(s)

Dance and party crowd; night clubs, sporting events, weddings

Font styles to use
Sans Serif

Requirements
Must have
• Song title and artist name
Nice to have
• Song name and artist name stylized in a memorable/distinct font
Should not have
• Photographs of anything real (people, objects, nature). Animated can be fine

```html
<!DOCTYPE html>
<html lang="en">
<head>
<meta charset="UTF-8">
<title>Carry the Tide (remix) – Derek Hanmore</title>
<link href="https://fonts.googleapis.com/css2?family=Press+Start+2P&display=swap" rel="stylesheet">
<style>
  :root {
    --deep-violet: #2a2380;
    --violet: #5b3bb0;
    --electric-blue: #1f8fe0;
    --cyan: #5fd3f5;
    --hot-pink: #ec6fa8;
    --red: #f2423a;
    --orange: #f7882a;
    --yellow: #ffe34a;
    --white-hot: #fff6c8;
    --ink: #0a0a0a;
  }
  * { margin: 0; padding: 0; box-sizing: border-box; }
  html, body { width: 1200px; height: 1200px; overflow: hidden; background: var(--deep-violet); }
  .cover {
    position: relative;
    width: 1200px;
    height: 1200px;
    overflow: hidden;
    font-family: "Press Start 2P", monospace;
  }
  .artwork {
    position: absolute;
    inset: 0;
    background: radial-gradient(circle at 50% 56%,
      var(--white-hot) 0%,
      var(--yellow) 12%,
      var(--orange) 24%,
      var(--red) 32%,
      var(--hot-pink) 38%,
      var(--cyan) 48%,
      var(--electric-blue) 62%,
      var(--violet) 78%,
      var(--deep-violet) 100%);
  }
  .cover-text {
    position: absolute;
    left: 0;
    width: 1200px;
    text-align: center;
    color: var(--ink);
    white-space: nowrap;
    font-weight: 400;
    line-height: 1;
  }
  .song-title {
    top: 560px;
    font-size: 58px;
    letter-spacing: 1px;
  }
  .song-version {
    top: 645px;
    font-size: 34px;
  }
  .artist-name {
    top: 752px;
    font-size: 32px;
  }
</style>
</head>
<body>
  <main class="cover">
    <div class="artwork" role="img" aria-label="Illustration area: a blazing sun setting over a rippling ocean, with vivid blue and violet light rays bursting outward"></div>
    <h1 class="cover-text song-title">CARRY THE TIDE</h1>
    <p class="cover-text song-version">(REMIX)</p>
    <p class="cover-text artist-name">DEREK HANMORE</p>
  </main>
</body>
</html>
```